Corewise Motion Business Cards

Can all designers please apply the following info on their designs' back-side of the business card: (please see brief file upload ('Info for backside...' - for required info, colours & layout)

SPECIALISING IN INDIVIDUAL PILATES INSTRUCTION
MATWORK – including small apparatus
and STUDIO:
VIVANTE 5 REFORMER
LADDER BARREL
MERIDAN BARREL
TENDRA DOME
KALVO CHAIR
TOR-I-VAN

Business Cards for Corewise Motion - applying the Corewise Motion logo design selected earlier.
Note the business card requires both a front and back side. Please refer to two uploaded ppt-files for type of info required to be displayed, and rough position of where info could be. Require innovative / fresh approach to business card design and use of colour by designers now. Please refer to and use logo as uploaded - also for potential business card colour application.

Dear Designers,

Please note the additional inclusion / upload of two draft ppt-files that try to show where I want what type of information, for both the front & back sides of the required business card, plus an attempt at showing the high-level concept / idea of business info position.

As my 'drafts' obviously lack colour and any ability towards innovative card design or approach – I now rely on your vastly superior graphic design abilities to produce a really great business card for my business…

Looking forward to your submissions!

Kind regards, Maren for: Corewise Motion 

Hello all Designers,

Can all designers please apply the following info on their designs' back-side of the business card: (please see / refer to the Brief and specifically the file upload ('Info for backside...' - for required info, colours & layout) - for the backside of the business card).

Info content (without colour, layout etc.):

and STUDIO:

VIVANTE 5 REFORMER

LADDER BARREL

MERIDAN BARREL

TENDRA DOME

KALVO CHAIR

TOR-I-VAN

Thank you to all designers that submitted for consideration!

With regards,

Corewise Motion

```html
<!DOCTYPE html>
<html lang="en">
<head>
<meta charset="utf-8">
<title>Corewise Motion – Business Card Front and Back</title>
<link rel="stylesheet" href="https://fonts.googleapis.com/css2?family=Open+Sans:wght@300;400;600;700&display=swap">
<style>
  :root {
    --stage: #e8e5e0;
    --green-light: #c6e67a;
    --green: #8fcb3a;
    --green-deep: #6cab22;
    --swoosh: #b5dc6a;
    --white: #ffffff;
    --orange: #ea6a2c;
    --ink: #3a3a3a;
    --grey: #5c5c5c;
  }
  * { margin: 0; padding: 0; box-sizing: border-box; }
  html, body {
    width: 1200px; height: 1023px; overflow: hidden;
    background: var(--stage);
    font-family: "Open Sans", Arial, sans-serif;
  }
  .canvas {
    width: 1200px; height: 1023px;
    display: flex; flex-direction: column;
    align-items: center; justify-content: center; gap: 64px;
  }
  .card { width: 620px; height: 354px; display: block;
          filter: drop-shadow(0 6px 14px rgba(0,0,0,.18)); }
  .brand-name { font-weight: 300; font-size: 30px; fill: var(--orange); }
  .person-name { font-weight: 700; font-size: 21px; fill: var(--orange); }
  .qualification { font-size: 12.5px; fill: var(--grey); }
  .contact { font-size: 14px; fill: var(--ink); }
  .address { font-weight: 600; font-size: 12.5px; letter-spacing: .4px; fill: var(--orange); }
  .tagline { font-weight: 600; font-size: 13px; letter-spacing: .8px; fill: var(--white); }
  .back-heading { font-weight: 700; font-size: 15px; letter-spacing: .3px; fill: var(--orange); }
  .back-item { font-size: 14px; letter-spacing: .4px; fill: var(--ink); }
  .icon-dot { fill: var(--orange); }
  .icon-line { fill: none; stroke: var(--white); stroke-width: 1.4; stroke-linecap: round; }
</style>
</head>
<body>
<main class="canvas">

  <!-- Front side -->
  <svg class="card card-front" viewBox="0 0 620 354" aria-label="Business card front">
    <defs>
      <linearGradient id="frontGreen" x1="0" y1="0" x2="1" y2="1">
        <stop offset="0" stop-color="var(--green-light)"/>
        <stop offset=".55" stop-color="var(--green)"/>
        <stop offset="1" stop-color="var(--green-deep)"/>
      </linearGradient>
      <clipPath id="frontClip"><rect width="620" height="354" rx="14"/></clipPath>
    </defs>
    <g clip-path="url(#frontClip)">
      <rect class="card-base" width="620" height="354" fill="url(#frontGreen)"/>
      <path class="swoosh-stripe" d="M330 0 C270 160 150 290 0 350" fill="none" stroke="var(--swoosh)" stroke-width="14" opacity=".85"/>
      <path class="white-panel" d="M360 0 H620 V262 C480 272 330 300 200 354 H40 C180 290 300 160 360 0 Z" fill="var(--white)"/>
      <path class="accent-rule" d="M620 262 C480 272 330 300 200 354" fill="none" stroke="var(--orange)" stroke-width="2.5"/>

      <g class="brand">
        <circle cx="36" cy="45" r="12" fill="var(--orange)"/>
        <text class="brand-name" x="56" y="56">Corewise Motion</text>
      </g>

      <g class="contact-block" text-anchor="end">
        <text class="person-name" x="592" y="46">Maren Lindqvarn</text>
        <text class="qualification" x="592" y="66">Dipl. of Professional Pilates Instruction</text>

        <text class="contact" x="568" y="104">041 555 0192</text>
        <text class="contact" x="568" y="128">info@corewisemotion.com</text>
        <text class="contact" x="568" y="152">www.corewisemotion.com.au</text>

        <text class="address" x="592" y="236">18 BRINDLE AVENUE, ASHGROVE WA 6090</text>
      </g>

      <g class="contact-icons">
        <g class="icon-phone">
          <circle class="icon-dot" cx="584" cy="99" r="8"/>
          <path class="icon-line" d="M581 95 q0 6 6 8"/>
        </g>
        <g class="icon-mail">
          <circle class="icon-dot" cx="584" cy="123" r="8"/>
          <path class="icon-line" d="M580 120 h8 v6 h-8 z M580 120 l4 3 l4 -3"/>
        </g>
        <g class="icon-web">
          <circle class="icon-dot" cx="584" cy="147" r="8"/>
          <circle class="icon-line" cx="584" cy="147" r="4.5"/>
          <path class="icon-line" d="M579.5 147 h9 M584 142.5 v9"/>
        </g>
      </g>

      <text class="tagline" x="592" y="334" text-anchor="end">BALANCE | STRENGTH | FLEXIBILITY</text>
    </g>
  </svg>

  <!-- Back side -->
  <svg class="card card-back" viewBox="0 0 620 354" aria-label="Business card back">
    <defs>
      <radialGradient id="backGreen" cx=".65" cy=".4" r=".85">
        <stop offset="0" stop-color="var(--green-light)"/>
        <stop offset=".6" stop-color="var(--green)"/>
        <stop offset="1" stop-color="var(--green-deep)"/>
      </radialGradient>
      <clipPath id="backClip"><rect width="620" height="354" rx="14"/></clipPath>
    </defs>
    <g clip-path="url(#backClip)">
      <rect class="card-base" width="620" height="354" fill="url(#backGreen)"/>

      <text class="back-heading" x="180" y="62">SPECIALISING IN INDIVIDUAL PILATES INSTRUCTION</text>

      <g class="service-list">
        <text class="back-item" x="220" y="100">MATWORK (INCL. SMALL APPARATUS)</text>
        <text class="back-item" x="220" y="124">STUDIO:</text>

        <circle class="icon-dot" cx="226" cy="143" r="3"/>
        <text class="back-item" x="236" y="148">VIVANTE 5 REFORMER</text>
        <circle class="icon-dot" cx="226" cy="167" r="3"/>
        <text class="back-item" x="236" y="172">LADDER BARREL</text>
        <circle class="icon-dot" cx="226" cy="191" r="3"/>
        <text class="back-item" x="236" y="196">MERIDAN BARREL</text>
        <circle class="icon-dot" cx="226" cy="215" r="3"/>
        <text class="back-item" x="236" y="220">TENDRA DOME</text>
        <circle class="icon-dot" cx="226" cy="239" r="3"/>
        <text class="back-item" x="236" y="244">KALVO CHAIR</text>
        <circle class="icon-dot" cx="226" cy="263" r="3"/>
        <text class="back-item" x="236" y="268">TOR-I-VAN</text>
      </g>
    </g>
  </svg>

</main>
</body>
</html>
```